Google Form Graphic to suit our Brand and industry

Create a graphic / image for us to put at the top of our client enquiry google form.
The image will be a section of an architectural home with our branding over the top. Preferably translucent.
The image must suit the shape of the google forms image, which is an elongated rectangle
#003d5d - brand colour

Target Market(s)

residential home owners, high end architectural homes

Industry/Entity Type

Residential construction

Colors
0054AA
0677BA
7BADD7
CADEEF
E8F1F8

Requirements
Must have
• our branding and a photo of an architectural home in the background

```html
<!DOCTYPE html>
<html lang="en">
<head>
<meta charset="utf-8">
<title>New Client Enquiry Form</title>
<link rel="stylesheet" href="https://fonts.googleapis.com/css2?family=Montserrat:wght@600&family=Roboto:wght@400;500&display=swap">
<style>
  :root {
    --page: #f6eee0;
    --card: #ffffff;
    --card-edge: #dedad3;
    --ink: #202124;
    --muted: #6b6b6b;
    --brand: #003d5d;
    --brand-mid: #0677ba;
    --accent-line: #7a6440;
    --focus: #4285f4;
    --badge: #e3bb62;
    --required: #d93025;
  }
  * { box-sizing: border-box; margin: 0; padding: 0; }
  html, body { width: 862px; height: 1200px; overflow: hidden; }
  body {
    background: var(--page);
    font-family: "Roboto", Arial, sans-serif;
    color: var(--ink);
    position: relative;
  }
  .header-banner {
    position: absolute; left: 32px; top: 13px;
    width: 800px; height: 199px;
    border-radius: 10px; overflow: hidden;
  }
  .header-banner svg { display: block; }
  .brand-name {
    position: absolute; left: 0; right: 0; top: 72px;
    text-align: center;
    font-family: "Montserrat", Arial, sans-serif;
    font-weight: 600; font-size: 52px; line-height: 54px; letter-spacing: 0.5px;
    color: var(--brand-mid);
    white-space: nowrap;
  }
  .card {
    position: absolute; left: 34px; width: 790px;
    background: var(--card);
    border: 1px solid var(--card-edge);
    border-radius: 8px;
  }
  .title-card { top: 272px; height: 171px; }
  .form-title {
    position: absolute; left: 25px; top: 25px;
    font-size: 30px; font-weight: 400; color: var(--ink);
  }
  .title-rule {
    position: absolute; left: 25px; top: 70px;
    width: 654px; height: 2px; background: var(--accent-line);
  }
  .card-actions { position: absolute; right: 34px; top: 26px; display: flex; gap: 32px; }
  .toolbar {
    position: absolute; left: 38px; top: 82px;
    display: flex; gap: 22px; align-items: center;
    font-size: 17px; color: #555;
  }
  .toolbar .tool { width: 20px; text-align: center; }
  .tool.bold { font-weight: 500; }
  .tool.italic { font-style: italic; font-family: Georgia, serif; }
  .tool.underline { text-decoration: underline; }
  .form-description {
    position: absolute; left: 25px; top: 126px;
    font-size: 14px; color: var(--ink);
  }
  .question { height: 141px; }
  .question.active { border-left: 6px solid var(--focus); }
  .question-label {
    position: absolute; left: 25px; top: 26px;
    font-size: 16px; color: var(--ink);
  }
  .question.active .question-label { left: 27px; }
  .required { color: var(--required); margin-left: 8px; }
  .answer-field {
    position: absolute; left: 25px; top: 72px; width: 370px;
    padding-bottom: 6px;
    font-size: 13.5px; letter-spacing: 0.3px; color: var(--muted);
    border-bottom: 1px dotted #9a9a9a;
  }
  .question.active .answer-field { left: 19px; }
  .q1 { top: 458px; }
  .q2 { top: 614px; }
  .q3 { top: 769px; }
  .q4 { top: 924px; }
  .section-flow {
    position: absolute; left: 33px; top: 1085px;
    display: flex; align-items: center;
    font-size: 14px; color: #444;
  }
  .section-flow .choice { margin-left: 18px; width: 330px; }
  .section-divider {
    position: absolute; left: 834px; top: 1089px;
    width: 1px; height: 111px; background: #c9c3b8;
  }
  .section-badge {
    position: absolute; left: 33px; top: 1165px;
    width: 124px; height: 44px; border-radius: 8px 8px 0 0;
    background: var(--badge);
    font-size: 13.5px; color: #333;
    padding: 10px 0 0 16px;
  }
</style>
</head>
<body>
  <header class="header-banner">
    <svg width="800" height="199" viewBox="0 0 800 199" role="img" aria-label="Photograph of a modern two-storey architectural home with large glass windows among trees, under a translucent navy brand panel">
      <defs>
        <linearGradient id="photoTone" x1="0" y1="0" x2="1" y2="1">
          <stop offset="0" stop-color="#f2f2f2"/>
          <stop offset="0.6" stop-color="#e4e5e6"/>
          <stop offset="1" stop-color="#d2d4d6"/>
        </linearGradient>
        <linearGradient id="navyTone" x1="0" y1="0" x2="1" y2="1">
          <stop offset="0" stop-color="#0c3656"/>
          <stop offset="1" stop-color="#0a2236"/>
        </linearGradient>
      </defs>
      <rect width="800" height="199" fill="url(#photoTone)"/>
      <polygon points="0,0 392,0 320,100 392,199 0,199" fill="url(#navyTone)"/>
    </svg>
    <div class="brand-name">VORELLIN HOMES</div>
  </header>

  <section class="card title-card">
    <h1 class="form-title">New Client Enquiry Form</h1>
    <div class="title-rule"></div>
    <div class="card-actions">
      <svg width="14" height="20" viewBox="0 0 14 20"><path d="M2 2l5 5 5-5M2 18l5-5 5 5" fill="none" stroke="#555" stroke-width="1.8"/></svg>
      <svg width="4" height="18" viewBox="0 0 4 18"><circle cx="2" cy="2" r="2" fill="#555"/><circle cx="2" cy="9" r="2" fill="#555"/><circle cx="2" cy="16" r="2" fill="#555"/></svg>
    </div>
    <div class="toolbar">
      <span class="tool bold">B</span>
      <span class="tool italic">I</span>
      <span class="tool underline">U</span>
      <svg class="tool" width="20" height="12" viewBox="0 0 20 12"><rect x="1" y="2" width="10" height="8" rx="4" fill="none" stroke="#555" stroke-width="1.6"/><rect x="9" y="2" width="10" height="8" rx="4" fill="none" stroke="#555" stroke-width="1.6"/></svg>
      <svg class="tool" width="18" height="18" viewBox="0 0 18 18"><path d="M2 3h14M9 3l-3 13M3 4l12 12" fill="none" stroke="#555" stroke-width="1.6"/></svg>
    </div>
    <p class="form-description">We would love to hear your thoughts or feedback on how we can improve your experience!</p>
  </section>

  <section class="card question active q1">
    <p class="question-label">Firstly, how did you hear about us?<span class="required">*</span></p>
    <div class="answer-field">Short answer text</div>
  </section>
  <section class="card question q2">
    <p class="question-label">Name</p>
    <div class="answer-field">Short answer text</div>
  </section>
  <section class="card question q3">
    <p class="question-label">Phone</p>
    <div class="answer-field">Short answer text</div>
  </section>
  <section class="card question q4">
    <p class="question-label">Email</p>
    <div class="answer-field">Short answer text</div>
  </section>

  <div class="section-flow">
    <span>After section 1</span>
    <span class="choice">Continue to next section</span>
    <svg width="10" height="6" viewBox="0 0 10 6"><path d="M0 0h10L5 6z" fill="#555"/></svg>
  </div>
  <div class="section-divider"></div>
  <div class="section-badge">Section 2 of 4</div>
</body>
</html>
```